Zielgruppe
Massagen und Therapien an Patienten mit Schmerzen an Muskeln und am gesamten Bewegungsapparat. Nachbehandlung nach Operationen und Verletzungen sowie Sportverletzungen therapieren.
Zielgruppe: alle Personen (m/w) jeden alters egal ob sportlich oder 'faul'.
Aufgabenstellung
Das Design soll Ruhe, Harmonie, Vertrautheit und Geborgenheit vermitteln. Es muß mit dem Firmenlogo harmonisieren (Farbe und Gestaltung).
Das Logo und der Text findet sich im Anhang.
Es können Bilder eigenständig hinzugefügt werden.
Unbedingt DIN-Format verwenden (welches bleibt dem Designer überlassen)

```html
<!DOCTYPE html>
<html lang="de">
<head>
<meta charset="utf-8">
<title>med. Massagepraxis Lindqvorst – Faltblatt</title>
<link href="https://fonts.googleapis.com/css2?family=Source+Sans+3:wght@400;600&display=swap" rel="stylesheet">
<style>
  :root {
    --teal: #1f9fb4;
    --wave-blue: #1a9ad6;
    --green-light: #e6f1d3;
    --green-mid: #a8cf6c;
    --green-deep: #7ab53a;
    --leaf: #9bc94a;
    --map-grey: #aaa8a9;
    --map-light: #b6b4b5;
    --pin-red: #d8343a;
    --ink: #1c1c1c;
    --paper: #ffffff;
  }
  * { margin: 0; padding: 0; box-sizing: border-box; }
  html, body { width: 1200px; height: 1139px; overflow: hidden; background: var(--paper); }
  body { font-family: "Source Sans 3", "Myriad Pro", sans-serif; color: var(--ink); }
  .flyer { position: relative; width: 1200px; height: 1139px; overflow: hidden; background: var(--paper); }

  .photo-massage {
    position: absolute; left: 0; top: 0; width: 395px; height: 640px;
    background: linear-gradient(170deg,
      #5f6a55 0%, #8a8f78 18%, #c7c2b4 32%, #e6d2c2 46%,
      #d6ab8e 58%, #c99677 68%, #e9d9cd 80%, #f6f3f0 100%);
  }
  .map-location {
    position: absolute; left: 395px; top: 0; width: 403px; height: 660px;
    background: linear-gradient(180deg, var(--map-light) 0%, var(--map-grey) 100%);
  }
  .map-pin { position: absolute; left: 634px; top: 246px; width: 28px; height: 36px; }

  .wave { position: absolute; left: 0; top: 0; width: 1200px; height: 1139px; }

  .brand-mark {
    position: absolute; left: 962px; top: 150px; width: 84px; height: 84px;
    border-radius: 50%; background: var(--leaf); opacity: .85;
  }
  .brand {
    position: absolute; left: 800px; top: 310px; width: 400px;
    text-align: center; color: var(--teal); font-size: 35px; line-height: 1.1; font-weight: 400;
  }

  .panel { position: absolute; }
  .panel-title { position: absolute; left: 106px; top: 586px; font-size: 42px; font-weight: 400; }
  .panel-intro { left: 24px; top: 660px; width: 360px; font-size: 14px; line-height: 19px; }
  .indications { left: 16px; top: 766px; width: 350px; font-size: 14px; line-height: 19.4px; }
  .indications h3 { font-size: 15px; font-weight: 600; line-height: 19px; }
  .indications ul { list-style: none; }
  .indications li { padding-left: 12px; position: relative; }
  .indications li::before { content: "•"; position: absolute; left: 1px; }
  .prescription { left: 24px; top: 1052px; width: 340px; font-size: 14px; line-height: 19px; }

  .contact { left: 418px; top: 764px; font-size: 21px; line-height: 38px; font-style: normal; }
  .contact .phone { margin-top: 8px; }

  .services { left: 842px; top: 640px; }
  .services h2 { font-size: 28px; font-weight: 400; margin-bottom: 52px; }
  .services ul { list-style: none; font-size: 22px; }
  .services li { height: 50px; }
  .services li:nth-child(4) { margin-top: 10px; }
  .services .house-calls { position: absolute; top: 400px; white-space: nowrap; font-size: 22px; }
</style>
</head>
<body>
<main class="flyer">
  <div class="photo-massage" role="img" aria-label="Foto: Therapeutin massiert den Rücken einer entspannt liegenden Patientin"></div>
  <div class="map-location" role="img" aria-label="Lageplan der Praxis mit umliegenden Straßen"></div>
  <svg class="map-pin" viewBox="0 0 28 36" aria-hidden="true">
    <path d="M14 1C7 1 2 6 2 13c0 9 12 22 12 22s12-13 12-22C26 6 21 1 14 1z" fill="var(--pin-red)" stroke="#fff" stroke-width="2"/>
    <circle cx="14" cy="13" r="4.5" fill="#fff"/>
  </svg>

  <svg class="wave" viewBox="0 0 1200 1139" aria-hidden="true">
    <defs>
      <linearGradient id="greenFade" x1="0" y1="0" x2="0" y2="1">
        <stop offset="0" stop-color="#ffffff"/>
        <stop offset="0.2" stop-color="#f6faef"/>
        <stop offset="0.45" stop-color="var(--green-light)"/>
        <stop offset="0.75" stop-color="var(--green-mid)"/>
        <stop offset="1" stop-color="var(--green-deep)"/>
      </linearGradient>
    </defs>
    <path d="M0,585 C200,555 400,650 610,646 C790,642 840,545 950,543 C1060,541 1140,590 1200,606 L1200,1139 L0,1139 Z" fill="url(#greenFade)"/>
    <path d="M0,585 C200,555 400,650 610,646 C790,642 840,545 950,543 C1060,541 1140,590 1200,606" fill="none" stroke="var(--wave-blue)" stroke-width="6"/>
  </svg>

  <div class="brand-mark" aria-hidden="true"></div>
  <div class="brand">med. Massagepraxis<br>Lindqvorst</div>

  <h1 class="panel-title">Massage</h1>
  <p class="panel panel-intro">Die klassische Massage dient vor allem zur Behandlung verspannter Muskulatur, oder zur Vorbeugung von Verspannungen.</p>

  <section class="panel indications">
    <h3>Indikationen:</h3>
    <ul>
      <li>Bewegungseinschränkung durch Verspannungen am Rücken, Brust, Schulter, etc...</li>
      <li>Spannungskopfschmerzen</li>
      <li>Muskelschmerzen</li>
      <li>zur schnellen Regeneration nach dem Sport oder nach Verletzungen</li>
      <li>fördert die seelische und körperliche Ausgeglichenheit</li>
      <li>stabilisiert das Immunsystem</li>
      <li>verbessert den Lymphfluss</li>
      <li>wirkt sich positiv auf die Durchblutung der Haut und des Bindegewebes aus</li>
    </ul>
  </section>
  <p class="panel prescription">Die Massagetherapie wird nach ärztlicher Verordnung durchgeführt.</p>

  <address class="panel contact">
    <div>med. Massagepraxis Lindqvorst</div>
    <div>Stefan Lindqvorst</div>
    <div>Amselweg 4 Haus 7</div>
    <div>3021 Lindenau</div>
    <div class="phone">Tel.: +43 660 000 12 34</div>
  </address>

  <section class="panel services">
    <h2>Ihr Spezialist für</h2>
    <ul>
      <li>Massage</li>
      <li>Lymphdrainage</li>
      <li>Akupunk-Massage nach Holzner</li>
      <li>EMS-Ganzkörpertraining</li>
    </ul>
    <p class="house-calls">Hausbesuche auf Anfrage</p>
  </section>
</main>
</body>
</html>
```